Label for Custom Gin Botle

Design an label for Gin botle, need label asap sorry

Target Market(s)

Our customers

Requirements
Must have
• Classic/expensive look

```html
<!DOCTYPE html>
<html lang="nl">
<head>
<meta charset="utf-8">
<title>Velden Crafters Gin – Label</title>
<link rel="stylesheet" href="https://fonts.googleapis.com/css2?family=Bebas+Neue&family=Playfair+Display:wght@900&family=Allura&display=swap">
<style>
  :root {
    --page: #ffffff;
    --label-green: #163a17;
    --label-green-deep: #0d2a0f;
    --label-green-light: #24502a;
    --accent-green: #3ff03f;
    --silver: #d9dcdc;
    --silver-dark: #8d9392;
    --white: #ffffff;
  }
  html, body {
    margin: 0;
    padding: 0;
    width: 1200px;
    height: 523px;
    overflow: hidden;
    background: var(--page);
  }
  .canvas {
    position: relative;
    width: 1200px;
    height: 523px;
  }
  .label {
    position: absolute;
    left: 45px;
    top: 45px;
    width: 1111px;
    height: 431px;
    overflow: hidden;
  }
  .label-background {
    position: absolute;
    inset: 0;
    background:
      radial-gradient(ellipse at 30% 40%, var(--label-green-light) 0%, transparent 55%),
      radial-gradient(ellipse at 75% 70%, var(--label-green-light) 0%, transparent 50%),
      linear-gradient(135deg, var(--label-green) 0%, var(--label-green-deep) 100%);
  }
  .artwork {
    position: absolute;
    border-radius: 45%;
    background: radial-gradient(circle, rgba(217,220,220,0.28) 0%, rgba(217,220,220,0.08) 70%);
  }
  .artwork-round { border-radius: 50%; }
  .artwork-square { border-radius: 6px; }
  .layout-lines {
    position: absolute;
    left: 0;
    top: 0;
  }
  .left-panel {
    position: absolute;
    left: 0;
    top: 0;
    width: 200px;
    height: 431px;
    font-family: "Bebas Neue", sans-serif;
    color: var(--white);
  }
  .brand-arc {
    position: absolute;
    left: 40px;
    top: 22px;
  }
  .spirit-type {
    position: absolute;
    left: 56px;
    top: 50px;
    font-size: 38px;
    letter-spacing: 7px;
    line-height: 1;
  }
  .warning-icon {
    position: absolute;
    left: 58px;
    width: 22px;
    height: 22px;
    border: 1.5px solid var(--white);
    background: rgba(255,255,255,0.35);
  }
  .warning-pregnancy { top: 106px; }
  .warning-driving { top: 137px; }
  .product-facts {
    position: absolute;
    left: 57px;
    top: 181px;
    font-size: 8px;
    letter-spacing: 0.9px;
    line-height: 11px;
  }
  .product-facts .volume { margin-bottom: 5px; }
  .stamp {
    position: absolute;
    left: 56px;
  }
  .stamp-batch { top: 228px; }
  .stamp-bottle { top: 305px; }
  .contact {
    position: absolute;
    left: 57px;
    top: 375px;
    font-size: 8px;
    letter-spacing: 0.9px;
    line-height: 10.5px;
  }
  .title-block {
    position: absolute;
    left: 0;
    top: 0;
  }
</style>
</head>
<body>
<main class="canvas">
  <section class="label" aria-label="Ginlabel Velden Crafters Gin">
    <div class="label-background" role="img" aria-label="Donkergroene gemarmerde achtergrond met vage getekende bouwgereedschappen"></div>

    <div class="artwork" role="img" aria-label="Zilveren lijntekening paradijsvogelbloem" style="left:200px;top:2px;width:183px;height:154px;"></div>
    <div class="artwork artwork-round" role="img" aria-label="Zilveren lijntekening bes" style="left:425px;top:29px;width:30px;height:30px;"></div>
    <div class="artwork artwork-round" role="img" aria-label="Zilveren lijntekening bes" style="left:195px;top:193px;width:36px;height:36px;"></div>
    <div class="artwork artwork-round" role="img" aria-label="Zilveren lijntekening halve limoen" style="left:766px;top:25px;width:97px;height:94px;"></div>
    <div class="artwork" role="img" aria-label="Zilveren lijntekening palmblad" style="left:944px;top:23px;width:138px;height:133px;"></div>
    <div class="artwork artwork-round" role="img" aria-label="Zilveren lijntekening bes" style="left:1013px;top:163px;width:36px;height:36px;"></div>
    <div class="artwork" role="img" aria-label="Zilveren lijntekening aardbei" style="left:226px;top:258px;width:92px;height:112px;"></div>
    <div class="artwork" role="img" aria-label="Zilveren lijntekening kleine aardbei" style="left:325px;top:346px;width:60px;height:63px;"></div>
    <div class="artwork artwork-square" role="img" aria-label="Zilveren lijntekening ijsblokje" style="left:688px;top:305px;width:50px;height:49px;"></div>
    <div class="artwork artwork-square" role="img" aria-label="Zilveren lijntekening ijsblokje" style="left:736px;top:349px;width:64px;height:55px;"></div>
    <div class="artwork" role="img" aria-label="Zilveren lijntekening hibiscusbloem" style="left:941px;top:289px;width:138px;height:122px;"></div>

    <svg class="layout-lines" width="1111" height="431" viewBox="0 0 1111 431" aria-hidden="true">
      <rect x="17" y="14" width="1078" height="404" rx="20" fill="none" stroke="var(--silver)" stroke-width="1.5"/>
      <path d="M483 173 V78 Q483 64 497 64 H734 Q748 64 748 78 V173" fill="none" stroke="var(--silver)" stroke-width="1.5"/>
      <path d="M483 251 V348 Q483 362 497 362 H734 Q748 362 748 348 V251" fill="none" stroke="var(--silver)" stroke-width="1.5"/>
    </svg>

    <svg class="title-block" width="1111" height="431" viewBox="0 0 1111 431" role="group" aria-label="Velden Crafters Gin">
      <defs>
        <linearGradient id="silverSheen" x1="0" y1="0" x2="1" y2="1">
          <stop offset="0" stop-color="#8d9392"/>
          <stop offset="0.45" stop-color="#f2f3f3"/>
          <stop offset="1" stop-color="#8d9392"/>
        </linearGradient>
      </defs>
      <text class="maker-name" x="616" y="126" text-anchor="middle" textLength="150" lengthAdjust="spacingAndGlyphs"
            font-family="'Playfair Display', serif" font-weight="900" font-size="34" fill="var(--accent-green)">VELDEN</text>
      <text class="product-name" x="616" y="242" text-anchor="middle" textLength="430" lengthAdjust="spacingAndGlyphs"
            font-family="'Playfair Display', serif" font-weight="900" font-size="80"
            fill="var(--accent-green)" stroke="var(--silver-dark)" stroke-width="1">CRAFTERS</text>
      <text class="product-script" x="612" y="318" text-anchor="middle"
            font-family="'Allura', cursive" font-size="118" fill="url(#silverSheen)">Gin</text>
    </svg>

    <div class="left-panel">
      <svg class="brand-arc" width="120" height="44" viewBox="0 0 120 44" aria-label="VELDEN.EU">
        <defs><path id="brandCurve" d="M6 40 Q60 6 114 40"/></defs>
        <text font-family="'Bebas Neue', sans-serif" font-size="19" fill="var(--white)" letter-spacing="1">
          <textPath href="#brandCurve" startOffset="50%" text-anchor="middle">VELDEN.EU</textPath>
        </text>
      </svg>
      <div class="spirit-type">GIN</div>

      <div class="warning-icon warning-pregnancy" role="img" aria-label="Pictogram: geen alcohol tijdens zwangerschap"></div>
      <div class="warning-icon warning-driving" role="img" aria-label="Pictogram: geen alcohol in het verkeer"></div>

      <div class="product-facts">
        <div class="volume">40% VOL. &nbsp;|&nbsp; 500ML</div>
        <div>KAN SPOREN VAN</div>
        <div>ALLERGENEN BEVATTEN</div>
      </div>

      <svg class="stamp stamp-batch" width="64" height="64" viewBox="0 0 64 64" aria-label="Batchnummer">
        <circle cx="32" cy="32" r="30" fill="var(--white)"/>
        <defs><path id="batchCurve" d="M12 30 A20 20 0 0 1 52 30"/></defs>
        <text font-family="'Bebas Neue', sans-serif" font-size="12" fill="var(--silver-dark)" letter-spacing="2">
          <textPath href="#batchCurve" startOffset="50%" text-anchor="middle">BATCH</textPath>
        </text>
      </svg>
      <svg class="stamp stamp-bottle" width="64" height="64" viewBox="0 0 64 64" aria-label="Flesnummer">
        <circle cx="32" cy="32" r="30" fill="var(--white)"/>
        <defs><path id="bottleCurve" d="M11 32 A21 21 0 0 1 53 32"/></defs>
        <text font-family="'Bebas Neue', sans-serif" font-size="12" fill="var(--silver-dark)" letter-spacing="2">
          <textPath href="#bottleCurve" startOffset="50%" text-anchor="middle">BOTTLE</textPath>
        </text>
      </svg>

      <address class="contact" style="font-style:normal;">
        <div>LINDELAAN 42</div>
        <div>7411 KM DEVENTER</div>
        <div>INFO@VELDEN-GIN.NL</div>
      </address>
    </div>
  </section>
</main>
</body>
</html>
```